Astrological planner&diary book cover.

Book cover for print paperback. Title: "Whole Stargazer Journal & Logbook – Sign One (Sign Two, Sign Three etc) 2022: Shape your days by charting Orbital and Night angles and passages, Idle Drift, Night cycles, Sky almanac, and Reversing bodies." The book is a series of Astrological diary & planner for 2022 for each Zodiac sign (12 books in total). The design template should be the same – the only difference would be the Zodiac sign image and text.
It should be neutral to positive. There is no restriction regarding the colors – it can be both B&W and full color.
The design should be original and not include any images which require obtaining a copyright license to use. Symbols in common use and not copyrighted are probably ok.
Text for the back cover is not yet available, will be ready by the end of the project. I will need PDF, JPEG, TIFF (all formats both in CMYK and RGB), and the source file. For CMYK, we need files with no color profiles assigned.
I have several options in my mind (But please do not limit yourself by these options - please feel free to suggest your vision):
1) Is Gradient morning clear sky and the star constellation and image at skyrise (like a rising star)
2) solid dark color with image and symbols of the Zodiac sign
75% of my auditory are women

```html
<!DOCTYPE html>
<html lang="en">
<head>
<meta charset="utf-8">
<title>Whole Stargazer Journal &amp; Logbook – Sign One 2022</title>
<link rel="stylesheet" href="https://fonts.googleapis.com/css2?family=Cinzel:wght@400;600&family=Montserrat:wght@300;600&display=swap">
<style>
  :root {
    --navy-deep: #02042a;
    --navy: #06105a;
    --glow: #1f5fe8;
    --cyan: #00b4f0;
    --glyph: #2ab4ff;
    --ink: #0a1140;
    --white: #ffffff;
    --line: #3b86ff;
  }
  html, body {
    margin: 0;
    padding: 0;
    width: 848px;
    height: 1200px;
    overflow: hidden;
    background: var(--navy-deep);
  }
  .cover {
    position: relative;
    width: 848px;
    height: 1200px;
    overflow: hidden;
    background:
      radial-gradient(ellipse 380px 430px at 426px 640px, rgba(31,95,232,0.55) 0%, rgba(10,30,140,0.35) 45%, rgba(3,6,49,0) 100%),
      radial-gradient(circle 120px at 426px 330px, rgba(40,110,255,0.45) 0%, rgba(3,6,49,0) 100%),
      linear-gradient(180deg, var(--navy-deep) 0%, #040a45 50%, var(--navy-deep) 100%);
  }
  .year-tab {
    position: absolute;
    left: 334px;
    top: 0;
    width: 181px;
    height: 89px;
    background: var(--cyan);
    display: flex;
    align-items: center;
    justify-content: center;
    font-family: "Montserrat", sans-serif;
    font-weight: 600;
    font-size: 50px;
    letter-spacing: 2px;
    color: var(--ink);
  }
  .series-line {
    position: absolute;
    left: 0;
    width: 848px;
    top: 106px;
    text-align: center;
    font-family: "Montserrat", sans-serif;
    font-weight: 600;
    font-size: 28px;
    letter-spacing: 1.8px;
    color: var(--white);
  }
  .sign-title {
    position: absolute;
    left: 0;
    width: 848px;
    top: 140px;
    margin: 0;
    text-align: center;
    font-family: "Cinzel", serif;
    font-weight: 400;
    font-size: 118px;
    line-height: 140px;
    color: var(--white);
  }
  .emblem {
    position: absolute;
    left: 0;
    top: 0;
  }
  .tagline {
    position: absolute;
    left: 78px;
    top: 880px;
    margin: 0;
    font-family: "Montserrat", sans-serif;
    font-weight: 300;
    font-size: 31px;
    line-height: 36px;
    color: var(--white);
  }
  .author-pill {
    position: absolute;
    left: 480px;
    top: 1042px;
    width: 368px;
    height: 75px;
    border-radius: 38px 0 0 38px;
    background: var(--cyan);
    display: flex;
    align-items: center;
    justify-content: center;
    font-family: "Cinzel", serif;
    font-weight: 600;
    font-size: 36px;
    color: var(--ink);
  }
</style>
</head>
<body>
<main class="cover">
  <div class="year-tab">2022</div>
  <div class="series-line">WHOLE STARGAZER JOURNAL &amp; LOGBOOK</div>
  <h1 class="sign-title">SIGN ONE</h1>

  <svg class="emblem" width="848" height="1200" viewBox="0 0 848 1200">
    <defs>
      <radialGradient id="symbolGlow" cx="50%" cy="50%" r="50%">
        <stop offset="0%" stop-color="#1e6bff" stop-opacity="0.7"/>
        <stop offset="100%" stop-color="#0a2aa0" stop-opacity="0.15"/>
      </radialGradient>
      <radialGradient id="figureFill" cx="55%" cy="45%" r="60%">
        <stop offset="0%" stop-color="#5fd0ff" stop-opacity="0.95"/>
        <stop offset="45%" stop-color="#2a9cff" stop-opacity="0.8"/>
        <stop offset="80%" stop-color="#1660e0" stop-opacity="0.45"/>
        <stop offset="100%" stop-color="#0b2b9a" stop-opacity="0"/>
      </radialGradient>
    </defs>

    <!-- sign symbol badge -->
    <circle class="badge-glow" cx="425" cy="344" r="54" fill="url(#symbolGlow)"/>
    <circle class="badge-ring" cx="425" cy="344" r="51" fill="none" stroke="#2f7dff" stroke-width="2" opacity="0.85"/>
    <circle class="badge-ring-inner" cx="425" cy="344" r="46" fill="none" stroke="#2f7dff" stroke-width="1" opacity="0.5"/>
    <path class="sign-glyph" d="M404 344 C393 331 398 318 409 319 C420 320 425 334 425 372 M446 344 C457 331 452 318 441 319 C430 320 425 334 425 372"
          fill="none" stroke="var(--glyph)" stroke-width="6" stroke-linecap="round" stroke-linejoin="round"/>

    <!-- large frame ring and triangle -->
    <circle cx="425" cy="672" r="259" fill="none" stroke="#2c8cff" stroke-width="4" opacity="0.9"/>
    <circle cx="425" cy="672" r="241" fill="none" stroke="#3a7bff" stroke-width="1" opacity="0.5"/>
    <polygon points="425,455 611,798 241,798" fill="none" stroke="var(--line)" stroke-width="1.5" opacity="0.6"/>

    <!-- zodiac figure area -->
    <rect class="figure-area" x="250" y="468" width="372" height="400" rx="120"
          fill="url(#figureFill)" role="img"
          aria-label="Glowing low-poly constellation illustration of the zodiac sign animal standing in profile"/>

    <!-- stars -->
    <g fill="#7fc4ff">
      <circle cx="185" cy="413" r="1.5"/><circle cx="365" cy="360" r="1.2"/>
      <circle cx="492" cy="375" r="1.5"/><circle cx="626" cy="462" r="2"/>
      <circle cx="140" cy="580" r="1.3"/><circle cx="700" cy="745" r="2"/>
      <circle cx="100" cy="680" r="1.2"/><circle cx="735" cy="590" r="1.3"/>
      <circle cx="250" cy="610" r="2"/><circle cx="606" cy="635" r="1.8"/>
      <circle cx="330" cy="460" r="1.5"/><circle cx="670" cy="860" r="1.3"/>
      <circle cx="130" cy="872" r="1.5"/><circle cx="760" cy="470" r="1.2"/>
    </g>
  </svg>

  <p class="tagline">Shape your days<br>by charting Orbital and<br>Night angles and passages,<br>Idle Drift, Night cycles,<br>Sky almanac, and<br>Reversing bodies.</p>

  <div class="author-pill">Author Name</div>
</main>
</body>
</html>
```